Invitation card for birthday of 10-year old

Design a birthday part invitation card for a 10-year old. The card should have a musical theme (the birthday girl is a pianist and vocalist).
Here is one of her social media pages: www.example-social.com/melodyfinchstage.
There are many images/videos of her here -- please include a picture of her from this page on the card.

The text for the card is:

LET'S PARTY (in large font)

JOIN US TO CELEBRATE
LINNEA'S 10th BIRTHDAY

482 BRAMBLECREST WAY, OAKVEND NJ 08163
2pm--6pm

```html
<!DOCTYPE html>
<html lang="en">
<head>
<meta charset="utf-8">
<title>Linnea's 10th Birthday Invitation</title>
<link rel="stylesheet" href="https://fonts.googleapis.com/css2?family=Allura&family=Montserrat:wght@300;400;500;600;800;900&display=swap">
<style>
  :root {
    --page-bg: #ece8df;
    --card-bg: #fdf8ec;
    --peach: #fad08a;
    --peach-soft: #fce3b4;
    --wave-tone: #fbe2a6;
    --rust: #c9501f;
    --rust-light: #d9652c;
    --teal: #4dbdb0;
    --teal-deep: #1f9c9c;
    --leaf-green: #587a2a;
    --magenta: #f0188f;
    --ink: #1c1c1c;
    --banner-text: #e0781c;
    --note-red: #b3331c;
    --sand: #e6d4c4;
    --gold-ring: #f7d35a;
    --photo-tone: #d9c2b4;
  }
  * { box-sizing: border-box; margin: 0; padding: 0; }
  html, body {
    width: 1200px; height: 800px; overflow: hidden;
    background: var(--page-bg);
  }
  .invitation {
    position: absolute; left: 336px; top: 30px;
    width: 528px; height: 740px;
    background: var(--card-bg);
    overflow: hidden;
    box-shadow: 0 6px 24px rgba(0,0,0,0.12);
    font-family: "Montserrat", sans-serif;
  }
  .invitation__backdrop { position: absolute; inset: 0; }
  .headline-lets {
    position: absolute; left: 196px; top: 52px;
    font-weight: 900; font-size: 46px; letter-spacing: 1px;
    color: var(--leaf-green); line-height: 1;
  }
  .headline-party {
    position: absolute; left: 130px; top: 70px;
    font-family: "Allura", cursive;
    font-size: 190px; line-height: 1; color: var(--ink);
  }
  .celebrant { position: absolute; left: 225px; top: 276px; width: 212px; }
  .celebrant__name {
    font-weight: 900; font-size: 40px; line-height: 1;
    color: var(--magenta); letter-spacing: -0.5px; white-space: nowrap;
  }
  .celebrant__age {
    margin-top: 10px; font-weight: 500; font-size: 27px; line-height: 1;
    color: var(--ink); white-space: nowrap;
  }
  .celebrant__age sup { font-size: 14px; vertical-align: 11px; }
  .celebrant__banner {
    margin-top: 8px; background: var(--peach);
    color: var(--banner-text); font-weight: 600; font-size: 13.5px;
    letter-spacing: 2px; line-height: 21px; text-align: center;
    white-space: nowrap;
  }
  .event-date {
    position: absolute; left: 336px; top: 410px; width: 114px;
    text-align: center; color: var(--leaf-green); line-height: 1;
  }
  .event-date__day { font-weight: 900; font-size: 74px; letter-spacing: -2px; }
  .event-date__month { font-weight: 900; font-size: 36px; margin-top: -2px; }
  .event-date__weekday { font-weight: 300; font-size: 14px; margin-top: 3px; letter-spacing: 0.5px; }
  .event-details {
    position: absolute; left: 300px; top: 540px; width: 186px;
    text-align: center; color: var(--ink);
  }
  .event-details__rule { height: 2px; width: 113px; margin: 0 auto 12px; background: var(--ink); }
  .event-details__address { font-size: 10.2px; line-height: 17px; font-weight: 400; white-space: nowrap; }
  .event-details__time { margin-top: 6px; font-size: 14px; font-weight: 700; }
  .music-note {
    position: absolute; color: var(--note-red);
    font-size: 22px; line-height: 1; font-family: "Montserrat", sans-serif;
  }
</style>
</head>
<body>
<main class="invitation">
  <svg class="invitation__backdrop" width="528" height="740" viewBox="0 0 528 740" xmlns="http://www.w3.org/2000/svg">
    <defs>
      <linearGradient id="wave-band" x1="0" y1="0" x2="0" y2="1">
        <stop offset="0" stop-color="#fbe2a6" stop-opacity="0.55"/>
        <stop offset="0.5" stop-color="#fbe2a6" stop-opacity="0.35"/>
        <stop offset="1" stop-color="#fbe2a6" stop-opacity="0.6"/>
      </linearGradient>
    </defs>
    <!-- wavy line band -->
    <rect role="img" aria-label="Pale yellow wavy line pattern" x="0" y="0" width="528" height="230" fill="url(#wave-band)"/>
    <!-- top-left peach wedge -->
    <polygon points="0,0 148,0 0,180" fill="var(--peach)"/>
    <polygon points="158,0 175,0 22,185 10,190" fill="var(--peach-soft)"/>
    <!-- top-right rust wave -->
    <path d="M353,0 L528,0 L528,170 C505,150 500,128 470,118 C440,108 415,98 400,70 C385,40 378,10 353,0 Z" fill="var(--rust-light)"/>
    <path d="M375,0 L528,0 L528,150 C510,130 495,105 468,98 C440,90 425,70 418,45 C410,20 395,8 375,0 Z" fill="var(--rust)"/>
    <!-- record note emblem -->
    <rect role="img" aria-label="Faint music note with record grooves emblem" x="88" y="255" width="107" height="125" rx="50" fill="var(--sand)" opacity="0.55"/>
    <!-- piano keys -->
    <rect role="img" aria-label="Piano keys illustration" x="0" y="375" width="76" height="80" rx="4" fill="#f1ebe4"/>
    <!-- saxophone -->
    <rect role="img" aria-label="Orange saxophone illustration" x="462" y="345" width="66" height="118" rx="18" fill="#f0961e"/>
    <!-- grid disc accent -->
    <circle cx="275" cy="457" r="34" fill="#5a8e8a" opacity="0.18"/>
    <!-- teal ring accent -->
    <g fill="none" stroke="var(--teal)" stroke-width="2.5">
      <circle cx="110" cy="600" r="38"/>
      <circle cx="110" cy="600" r="28"/>
      <circle cx="110" cy="600" r="18"/>
    </g>
    <!-- photo frame -->
    <rect x="84" y="400" width="220" height="273" rx="110" fill="var(--card-bg)" stroke="var(--gold-ring)" stroke-width="3"/>
    <rect role="img" aria-label="Photo of the birthday girl holding a flower" x="95" y="411" width="199" height="253" rx="99" fill="var(--photo-tone)"/>
    <!-- bottom-left teal wave -->
    <path d="M0,605 C40,598 55,630 70,652 C90,680 120,662 150,670 C190,680 220,715 283,740 L0,740 Z" fill="var(--teal)"/>
    <path d="M0,640 C30,640 50,665 75,690 C100,712 140,700 180,712 C205,720 225,732 240,740 L0,740 Z" fill="var(--teal-deep)"/>
    <!-- bottom-right peach wedge -->
    <polygon points="528,620 528,740 283,740" fill="var(--peach)"/>
    <polygon points="528,600 528,612 270,740 250,740" fill="var(--peach-soft)"/>
    <rect role="img" aria-label="Faint wavy line pattern" x="434" y="690" width="94" height="40" fill="#fdf1d6" opacity="0.7"/>
    <!-- dot grid -->
    <rect role="img" aria-label="Teal dot grid pattern" x="192" y="697" width="142" height="33" fill="var(--teal-deep)" opacity="0.18"/>
  </svg>

  <h1 class="headline">
    <span class="headline-lets">LET’S</span>
    <span class="headline-party">Party</span>
  </h1>

  <section class="celebrant">
    <p class="celebrant__name">LINNEA’S</p>
    <p class="celebrant__age">10<sup>TH</sup> BIRTHDAY</p>
    <p class="celebrant__banner">JOIN US TO CELEBRATE</p>
  </section>

  <section class="event-date">
    <p class="event-date__day">16</p>
    <p class="event-date__month">DEC</p>
    <p class="event-date__weekday">SATURDAY</p>
  </section>

  <section class="event-details">
    <div class="event-details__rule"></div>
    <p class="event-details__address">482 BRAMBLECREST WAY,<br>OAKVEND NJ 08163</p>
    <p class="event-details__time">2pm-6pm</p>
  </section>

  <span class="music-note" style="left:50px;top:250px">♪</span>
  <span class="music-note" style="left:30px;top:292px">♫</span>
  <span class="music-note" style="left:64px;top:350px">♪</span>
  <span class="music-note" style="left:446px;top:228px">♫</span>
  <span class="music-note" style="left:482px;top:272px">♫</span>
  <span class="music-note" style="left:476px;top:340px">♫</span>
  <span class="music-note" style="left:46px;top:515px">♫</span>
  <span class="music-note" style="left:18px;top:562px">♪</span>
  <span class="music-note" style="left:481px;top:528px">♪</span>
  <span class="music-note" style="left:475px;top:605px">♪</span>
  <span class="music-note" style="left:328px;top:646px">♪</span>
  <span class="music-note" style="left:386px;top:643px">♫</span>
</main>
</body>
</html>
```